A building General Contractor is looking for a business card design

I need a business card designed. The company "Crestline Structure Builders" is a general contractor for commercial buildings and pre-engineered metal buildings.

```html
<!DOCTYPE html>
<html lang="en">
<head>
<meta charset="utf-8">
<title>Crestline Structure Builders – Business Card</title>
<link href="https://fonts.googleapis.com/css2?family=Arimo:wght@400;700&display=swap" rel="stylesheet">
<style>
  :root {
    --stage: #262626;
    --card-black: #050505;
    --card-white: #ffffff;
    --ink-light: #ffffff;
    --ink-soft: #d9d9d9;
    --rule: #8a8a8a;
  }
  * { margin: 0; padding: 0; box-sizing: border-box; }
  html, body {
    width: 1200px; height: 1015px; overflow: hidden;
    background: var(--stage);
    font-family: "Arimo", Arial, sans-serif;
  }
  .canvas { position: relative; width: 1200px; height: 1015px; }
  .card {
    position: absolute; left: 220px; width: 760px; height: 434px;
    background: var(--card-black); overflow: hidden;
    box-shadow: 0 18px 40px rgba(0,0,0,.55);
  }
  .card--front { top: 48px; }
  .card--back { top: 533px; }

  /* Front */
  .brand {
    position: absolute; inset: 0;
    display: flex; align-items: center; justify-content: center; gap: 22px;
  }
  .brand__square { width: 46px; height: 46px; background: var(--ink-light); flex: none; }
  .brand__name {
    color: var(--ink-light); font-weight: 700; font-size: 40px;
    line-height: 1.05; letter-spacing: 1px; text-transform: uppercase;
  }

  /* Back */
  .back__panel { position: absolute; inset: 0; width: 100%; height: 100%; }
  .contact {
    position: absolute; left: 395px; top: 78px; right: 30px; color: var(--ink-light);
  }
  .contact__name { font-weight: 700; font-size: 30px; letter-spacing: .5px; text-transform: uppercase; }
  .contact__title { font-size: 21px; color: var(--ink-soft); margin-top: 4px; }
  .contact__rule { width: 120px; height: 1px; background: var(--rule); margin: 18px 0 16px; }
  .contact__list { list-style: none; font-size: 21px; line-height: 1.45; }
  .contact__list li { display: flex; align-items: center; gap: 10px; white-space: nowrap; }
  .contact__list svg { width: 20px; height: 20px; flex: none; }
  .contact__address { font-size: 21px; line-height: 1.35; }
</style>
</head>
<body>
<main class="canvas">
  <section class="card card--front" aria-label="Card front">
    <div class="brand">
      <span class="brand__square"></span>
      <span class="brand__name">Crestline Structure<br>Builders</span>
    </div>
  </section>

  <section class="card card--back" aria-label="Card back">
    <svg class="back__panel" viewBox="0 0 760 434" preserveAspectRatio="none" aria-hidden="true">
      <polygon points="0,0 250,0 350,434 0,434" fill="var(--card-white)"/>
    </svg>
    <div class="contact">
      <h1 class="contact__name">Daniel Harlow</h1>
      <p class="contact__title">Managing Director</p>
      <div class="contact__rule"></div>
      <ul class="contact__list">
        <li>
          <svg viewBox="0 0 24 24"><path fill="#fff" d="M6.6 10.8a15 15 0 0 0 6.6 6.6l2.2-2.2c.3-.3.7-.4 1-.2 1.1.4 2.3.6 3.6.6.6 0 1 .4 1 1V20c0 .6-.4 1-1 1A17 17 0 0 1 3 4c0-.6.4-1 1-1h3.5c.6 0 1 .4 1 1 0 1.3.2 2.5.6 3.6.1.3 0 .7-.2 1z"/></svg>
          044-555 010 234
        </li>
        <li>
          <svg viewBox="0 0 24 24"><rect x="2" y="5" width="20" height="14" fill="none" stroke="#fff" stroke-width="2"/><path d="M2 5l10 8 10-8" fill="none" stroke="#fff" stroke-width="2"/></svg>
          info@crestlinesb.com
        </li>
        <li>
          <svg viewBox="0 0 24 24" fill="none" stroke="#fff" stroke-width="2"><circle cx="12" cy="12" r="9"/><path d="M3 12h18M12 3c3 3 3 15 0 18M12 3c-3 3-3 15 0 18"/></svg>
          www.crestlinesb.com
        </li>
      </ul>
      <div class="contact__rule"></div>
      <p class="contact__address">88 Foundry Road, Unit 4<br>30917, Riverton</p>
    </div>
  </section>
</main>
</body>
</html>
```